Business Advisory Firm Business Card

A clean, very upscale looking business card. Not crowded.

Please include logo (attached) and:

Daria K. Pellworth
Four Marlow Court
New York, NY 10023
tel: (917) 555-0143
fax: (646) 555-0172
email: dpellworth@quarrystoneconsultants.example
website: www.quarrystoneconsultants.example

Target Market(s)

Business clients. Often real estate development firms, other advisory firms or growing companies that need assistance. I would like a card that looks impressive and confident.

Industry/Entity Type

Business

Colors

Designer to choose colors to be used in the design.

Requirements
Must have
• Impressive and confident. Please include logo.
Should not have
• nothing flashy...

```html
<!DOCTYPE html>
<html lang="en">
<head>
<meta charset="utf-8">
<title>Quarrystone Advisory Services – Business Card</title>
<link href="https://fonts.googleapis.com/css2?family=Arvo:wght@700&family=Crimson+Text:wght@600&display=swap" rel="stylesheet">
<style>
  :root {
    --backdrop: #2b2d30;
    --card-charcoal: #1f2022;
    --card-charcoal-light: #38393c;
    --panel-white: #ffffff;
    --panel-grey: #dcdcdc;
    --ribbon-green: #3cb54a;
    --ribbon-shadow: #2a8436;
    --brand-green: #8cc63f;
    --ink-dark: #1b1b1b;
    --ink-light: #f4f4f4;
  }
  * { box-sizing: border-box; margin: 0; padding: 0; }
  html, body { width: 1200px; height: 900px; overflow: hidden; }
  body {
    background: var(--backdrop);
    display: flex;
    align-items: center;
    justify-content: center;
  }
  .business-card {
    position: relative;
    width: 1050px;
    height: 600px;
    border-radius: 44px;
    overflow: hidden;
    background: radial-gradient(ellipse at 55% 40%, var(--card-charcoal-light) 0%, var(--card-charcoal) 75%);
    box-shadow: 0 18px 40px rgba(0,0,0,0.45);
  }
  .brand-panel {
    position: absolute;
    left: 0; top: 0;
    width: 390px; height: 470px;
    border-radius: 0 0 44px 0;
    background: radial-gradient(ellipse at 50% 35%, var(--panel-white) 45%, var(--panel-grey) 100%);
    display: flex;
    flex-direction: column;
    align-items: center;
    justify-content: flex-end;
    padding-bottom: 56px;
  }
  .brand-square {
    width: 150px; height: 150px;
    background: var(--brand-green);
    margin-bottom: 44px;
  }
  .brand-name {
    font-family: "Arvo", serif;
    font-weight: 700;
    font-size: 38px;
    line-height: 1.05;
    color: var(--ink-dark);
    text-align: left;
  }
  .name-ribbon {
    position: absolute;
    left: 500px; right: 0; top: 62px;
    height: 96px;
    background: var(--ribbon-green);
    border-radius: 14px 0 0 0;
    box-shadow: 0 6px 0 var(--ribbon-shadow);
    display: flex;
    align-items: center;
    padding-left: 40px;
  }
  .person-name {
    font-family: "Arvo", serif;
    font-weight: 700;
    font-size: 44px;
    color: var(--ink-light);
    letter-spacing: 1px;
  }
  .contact-list {
    position: absolute;
    left: 490px; top: 318px;
    list-style: none;
  }
  .contact-item {
    display: flex;
    align-items: center;
    height: 54px;
    font-family: "Crimson Text", serif;
    font-weight: 600;
    font-size: 25px;
    color: var(--ink-light);
    white-space: nowrap;
  }
  .contact-icon {
    width: 30px; height: 30px;
    margin-right: 22px;
    flex: none;
  }
  .contact-icon * { fill: none; stroke: var(--ink-light); stroke-width: 2.4; stroke-linejoin: round; }
  .fax { margin-left: 28px; }
</style>
</head>
<body>
  <div class="business-card">
    <div class="brand-panel">
      <div class="brand-square"></div>
      <p class="brand-name">Quarrystone<br>Advisory<br>Services, inc.</p>
    </div>

    <div class="name-ribbon">
      <h1 class="person-name">Daria K. Pellworth</h1>
    </div>

    <ul class="contact-list">
      <li class="contact-item">
        <svg class="contact-icon" viewBox="0 0 30 30" aria-hidden="true"><path d="M3 15 L15 4 L27 15 M7 12 V26 H23 V12 M13 26 V19 H17 V26"/></svg>
        Four Marlow Court, New York, NY 10023
      </li>
      <li class="contact-item">
        <svg class="contact-icon" viewBox="0 0 30 30" aria-hidden="true"><rect x="8" y="3" width="14" height="24" rx="3"/><rect x="11" y="7" width="8" height="8"/></svg>
        (917) 555-0143 ;<span class="fax">Fax: (646) 555-0172 ;</span>
      </li>
      <li class="contact-item">
        <svg class="contact-icon" viewBox="0 0 30 30" aria-hidden="true"><rect x="3" y="7" width="24" height="17"/><path d="M3 7 L15 17 L27 7"/></svg>
        dpellworth@quarrystoneconsultants.example
      </li>
      <li class="contact-item">
        <svg class="contact-icon" viewBox="0 0 30 30" aria-hidden="true"><circle cx="15" cy="15" r="11"/><path d="M4 15 H26 M15 4 C9 10 9 20 15 26 M15 4 C21 10 21 20 15 26"/></svg>
        www.quarrystoneconsultants.example
      </li>
    </ul>
  </div>
</body>
</html>
```